DL FLYER - Stroll Sip Nibble Outings

I need a2-sided DL flyer designed to put into Hotel foyers. This will need to stand out as it will be in a rack with multiple other options.

Our tours are all about walking with us to take in great venues for food and beverages with art and history along the way.

We operate in Perth City plus Fremantle.

I am hoping for the flyer to look something like my website - https://strollsipnibble.example.au/

This website will be updated in the coming weeks with new experiences and a new booking platform.

I want the flyers to be used to drive bookings from the updated website.

Attached are several images that could be used also.

Target Market(s)

Social groups, couples, friends groups & foodies!

Industry/Entity Type

Food & Beverage Walking Tours

Font styles to use
Serif
Sans Serif
Decorative
Script

Colors
0094D4
00A9DD
6FCCEA
C7EBF8
E9F6FB
59FF00
82FF00
B8FF75
E3FFCB
F4FFEA
FFF300
FFF600
FEFA6F
FFFEC7
FFFEE8
F0912C
F2A743
F7CA91
FBE8D2
FDF5EE

Requirements
Must have
• Logo and must look fun. Discount code - CITYLOVESU for online price 15% off (not valid on gift voucher purchases)
Nice to have
• similar to my website - colours and styling. I will be updating available tours, costs and timing in the coming weeks. Check out my new booking link to get pricing and tour details - https://www-902k.tixlane.example/tixlane/b_strollsipnibbleoutings_start.html?ctlsrc2=Qm518LMNAB3JKty7GhqwZr4xcV%2F9P8ArbdwHn%2FUsPw%3D&src=07k
Should not have
• .

```html
<!DOCTYPE html>
<html lang="en">
<head>
<meta charset="utf-8">
<title>Stroll Sip Nibble Outings – DL Flyer</title>
<link rel="stylesheet" href="https://fonts.googleapis.com/css2?family=Unbounded:wght@700;800&family=Montserrat:wght@500;600;700&display=swap">
<style>
  :root{
    --stage:#b3b3b3;
    --cream:#f7f4e3;
    --ink:#1f302d;
    --orange:#ef6220;
    --mint:#9ed7a4;
    --mint-deep:#2f9e6e;
    --pink:#f4d8d0;
    --butter:#f3f0cf;
    --photo-warm:#a9553a;
    --photo-food:#c98b5a;
    --photo-bar:#5a4a3e;
  }
  *{box-sizing:border-box;margin:0;padding:0}
  html,body{width:1200px;height:900px;overflow:hidden;background:var(--stage)}
  body{position:relative;font-family:"Montserrat",sans-serif;color:var(--ink)}
  .display{font-family:"Unbounded",sans-serif;font-weight:800;text-transform:uppercase;line-height:1.05}

  .flyer{position:absolute;top:45px;width:380px;height:810px;overflow:hidden;box-shadow:0 8px 22px rgba(0,0,0,.25)}
  .flyer--front{left:195px;background:var(--cream)}
  .flyer--back{left:625px;background:var(--pink)}

  /* FRONT */
  .brand{position:absolute;top:0;left:0;right:0;height:290px}
  .brand-scene{position:absolute;top:34px;left:40px;right:40px;height:200px;border-radius:110px 110px 24px 24px;background:linear-gradient(180deg,#f1e6d6 0%,#e9c9c2 55%,#a8d9ae 100%)}
  .brand-name{position:absolute;left:0;right:0;bottom:22px;display:flex;align-items:center;justify-content:center;gap:8px;font-family:"Montserrat",sans-serif;font-weight:700;font-size:17px;letter-spacing:.02em;color:var(--ink)}
  .brand-mark{width:12px;height:12px;background:var(--ink);flex:none}

  .features{position:absolute;top:290px;left:0;right:0;height:405px;background:var(--ink)}
  .splash{position:absolute;right:-30px;top:-40px;width:130px;height:150px;border-radius:55% 45% 50% 60%;background:var(--butter)}
  .feature-list{position:absolute;top:36px;left:28px;list-style:none;display:flex;flex-direction:column;gap:18px}
  .feature{display:flex;align-items:center;gap:16px}
  .feature-icon{width:50px;height:50px;border-radius:50%;background:var(--mint);display:flex;align-items:center;justify-content:center;flex:none}
  .feature-text{font-size:19px;color:var(--cream)}
  .accent-orange{color:var(--orange)}
  .accent-mint{color:var(--mint)}
  .accent-butter{color:var(--butter)}

  .photos{position:absolute;bottom:20px;left:18px;right:18px;display:flex;gap:10px;align-items:flex-end}
  .photo{flex:1;border-radius:18px;border:3px solid var(--mint)}
  .photo--diners{height:104px;background:linear-gradient(135deg,var(--photo-warm),#d9a27e)}
  .photo--dishes{height:116px;background:linear-gradient(135deg,var(--photo-food),#e8e2d6)}
  .photo--bar{height:128px;background:linear-gradient(135deg,var(--photo-bar),#8f7b62)}

  .contact{position:absolute;bottom:0;left:0;right:0;height:115px;background:var(--pink);display:flex;flex-direction:column;justify-content:center;align-items:center;gap:3px;text-align:center}
  .contact-line{font-family:"Unbounded",sans-serif;font-weight:700;font-size:15px}
  .contact-line--email{font-size:13px}
  .contact-line--web{font-size:17px;font-weight:800}

  /* BACK */
  .about{position:absolute;top:0;left:0;right:0;height:345px;padding:44px 30px 0}
  .cutlery-art{position:absolute;top:22px;right:28px;width:52px;height:52px;border-radius:50%;background:linear-gradient(135deg,var(--orange),var(--ink))}
  .section-title{display:inline-block;font-size:19px;padding:2px 8px;background:linear-gradient(transparent 45%,var(--mint) 45%)}
  .about-copy{margin-top:14px;font-size:11.5px;font-weight:500;line-height:1.45;display:flex;flex-direction:column;gap:9px}

  .tours{position:absolute;top:345px;left:0;right:0;height:310px;background:var(--mint);border-radius:0 0 26px 26px;padding:28px 24px 0}
  .tours-title{display:inline-block;background:var(--orange);color:var(--cream);font-size:15px;padding:8px 14px;border-radius:20px}
  .tour-list{list-style:none;margin-top:20px;display:flex;flex-direction:column;gap:16px}
  .tour{display:grid;grid-template-columns:1fr 74px 96px;align-items:center;column-gap:6px}
  .tour-name{font-size:12px}
  .tour-price{font-size:24px;color:var(--orange)}
  .tour-when{font-size:9px;line-height:1.25}

  .discount{position:absolute;bottom:0;left:0;right:0;height:155px;display:flex;flex-direction:column;align-items:center;justify-content:center;gap:8px}
  .splash--corner{position:absolute;left:-40px;bottom:-30px;width:110px;height:120px;border-radius:50% 60% 45% 55%;background:var(--butter)}
  .discount-row{display:flex;align-items:center;gap:10px;position:relative}
  .discount-label{font-size:12px;text-align:right}
  .discount-code{background:var(--orange);color:var(--cream);font-size:24px;padding:6px 14px;border-radius:18px}
  .discount-terms{font-size:11.5px;font-weight:600;text-align:center;line-height:1.35;position:relative}
</style>
</head>
<body>

<section class="flyer flyer--front" aria-label="Flyer front">
  <header class="brand">
    <div class="brand-scene" role="img" aria-label="Illustrated city skyline with a group of walkers"></div>
    <h1 class="brand-name"><span class="brand-mark"></span>Stroll Sip Nibble Outings</h1>
  </header>

  <div class="features">
    <div class="splash" role="img" aria-label="Dotted cream splash decoration"></div>
    <ul class="feature-list">
      <li class="feature">
        <span class="feature-icon">
          <svg width="26" height="26" viewBox="0 0 24 24" fill="none" stroke="#ef6220" stroke-width="2.2"><path d="M12 22s7-7 7-12a7 7 0 0 0-14 0c0 5 7 12 7 12z"/><circle cx="12" cy="10" r="2.5"/></svg>
        </span>
        <p class="feature-text display"><span class="accent-orange">Explore</span><br>the city</p>
      </li>
      <li class="feature">
        <span class="feature-icon">
          <svg width="28" height="28" viewBox="0 0 24 24" fill="none" stroke="#ef6220" stroke-width="2"><path d="M4 5h16v11H10l-5 4v-4H4z"/><circle cx="8.5" cy="10.5" r="1" fill="#ef6220"/><circle cx="12" cy="10.5" r="1" fill="#ef6220"/><circle cx="15.5" cy="10.5" r="1" fill="#ef6220"/></svg>
        </span>
        <p class="feature-text display"><span class="accent-mint">Meet</span> new<br>people</p>
      </li>
      <li class="feature">
        <span class="feature-icon">
          <svg width="28" height="28" viewBox="0 0 24 24" fill="none" stroke="#ef6220" stroke-width="2"><path d="M3 13h18a9 6 0 0 1-18 0z"/><path d="M9 4c-1 2 1 3 0 6M13 4c-1 2 1 3 0 6"/></svg>
        </span>
        <p class="feature-text display"><span class="accent-butter">Enjoy</span> great<br>food</p>
      </li>
    </ul>
    <div class="photos">
      <div class="photo photo--diners" role="img" aria-label="Photo of guests laughing over drinks"></div>
      <div class="photo photo--dishes" role="img" aria-label="Photo of shared dishes on a table"></div>
      <div class="photo photo--bar" role="img" aria-label="Photo of a guide talking at a bar"></div>
    </div>
  </div>

  <footer class="contact">
    <p class="contact-line">0400 123 456</p>
    <p class="contact-line contact-line--email">perth@strollsipnibble.example.au</p>
    <p class="contact-line contact-line--web">STROLLSIPNIBBLE.EXAMPLE.AU</p>
  </footer>
</section>

<section class="flyer flyer--back" aria-label="Flyer back">
  <div class="about">
    <div class="cutlery-art" role="img" aria-label="Illustrated fork and spoon icon"></div>
    <h2 class="section-title display">About us</h2>
    <div class="about-copy">
      <p>Step off the tourist trail, leave the beaten track behind, do something different in a region near you and see the secret spots that locals love.</p>
      <p>We take our walking tours down the back streets, underneath and above plus through the alleyways, to share great food and beverages with our groups.</p>
      <p>Go with our guides to try modern Australian fare. All served with lashings of history about each city you tour.</p>
      <p>We have private tours for ready-made groups and our regular tours for people who are ready to mingle.</p>
    </div>
  </div>

  <div class="tours">
    <h2 class="tours-title display">Tours &amp; Experiences</h2>
    <ul class="tour-list">
      <li class="tour"><span class="tour-name display">Twilight supper stroll</span><span class="tour-price display">$85</span><span class="tour-when display">Perth<br>Sat 4-7pm</span></li>
      <li class="tour"><span class="tour-name display">Weekend harbour grazing</span><span class="tour-price display">$75</span><span class="tour-when display">Fremantle<br>Sun 3-6pm</span></li>
      <li class="tour"><span class="tour-name display">Grill &amp; ale trail</span><span class="tour-price display">$85</span><span class="tour-when display">Perth<br>Sat 11am</span></li>
      <li class="tour"><span class="tour-name display">Market basket ramble</span><span class="tour-price display">$80</span><span class="tour-when display">Fremantle<br>Sat 1-4pm</span></li>
    </ul>
  </div>

  <div class="discount">
    <div class="splash--corner" role="img" aria-label="Dotted cream splash decoration"></div>
    <div class="discount-row">
      <span class="discount-label display">Discount<br>code</span>
      <span class="discount-code display">CITYLOVESU</span>
    </div>
    <p class="discount-terms">for online price 15% off<br>(not valid on gift voucher purchases)</p>
  </div>
</section>

</body>
</html>
```